App Design Project NDA enclosed

I currently have an iphone and Android application developed. I found there was an issue with my overall business strategy. As a result, I have restructured the UI layout and functionality of the app. In doing so, I have the need for 25+ additional screen shots to be developed, (with the possibility to redo the current app design). There is a lot of detail in this process, so please contact me to get any clarity you need. I have sketches and such and I am happy to provide those for you, but I don't want to just upload those to anyone - I have need NDA's signed before moving forward on this.
So - the name of the application is: Cool Nookz. Cool Nookz is a mobile dating application. I am happy to upload to you all that I currently have so you can get a feel for the direction as well as the features and functions of the app. The only thing I am able to upload is the current logo (which may need a revision as well)
Please contact me with any an all questions - I am prepared to compensate the right designer for their time on this project.
The only mobile dating application that we are considering being a tough competitor is BRVenus - I like their function and layout. I don't like Plimb or Vrask - We are more Pairly.net - quality, without the sleezy hookup edge. The demographic is broad from F/M 18-30 , F/M 31-40 and then F/M 40+ I will send you everything we have if you are willing to sign an NDA and be willing to look at our application and current storyboard.
Please email back to dan@coolnookz.example

```html
<!DOCTYPE html>
<html lang="en">
<head>
<meta charset="utf-8">
<title>Cool Nookz – Home Screen Variations</title>
<link rel="stylesheet" href="https://fonts.googleapis.com/css2?family=Lato:wght@400;700;900&family=Cormorant+Garamond:wght@500&family=Nunito:wght@700;800&display=swap">
<style>
  :root {
    --page: #ffffff;
    --red: #c21a2c;
    --red-dark: #8e1320;
    --red-deep: #6f0e18;
    --cream: #f6f1e4;
    --tan: #b3a584;
    --ink: #3a3a3a;
    --muted: #666666;
    --gold: #c9a54a;
    --ad-green: #0f7a3e;
    --ad-green-light: #3f9b45;
    --shop-yellow: #f2c200;
    --status-bg: #000000;
  }
  * { box-sizing: border-box; margin: 0; padding: 0; }
  html, body { width: 1200px; height: 644px; overflow: hidden; }
  body {
    background: var(--page);
    display: flex;
    align-items: center;
    justify-content: center;
    gap: 30px;
    font-family: "Lato", sans-serif;
  }
  .defs { position: absolute; width: 0; height: 0; }

  .screen {
    width: 270px;
    height: 405px;
    display: flex;
    flex-direction: column;
    background: #000;
    box-shadow: 0 2px 8px rgba(0,0,0,.25);
  }

  /* status bar */
  .status-bar {
    height: 16px;
    background: var(--status-bg);
    color: #fff;
    font: 700 8.5px "Lato", sans-serif;
    display: flex;
    align-items: center;
    justify-content: space-between;
    padding: 0 6px;
  }
  .status-left { display: flex; align-items: center; gap: 3px; }
  .signal { display: flex; align-items: flex-end; gap: 1px; height: 7px; }
  .signal i { display: block; width: 1.6px; background: #fff; }
  .signal i:nth-child(1) { height: 2px; }
  .signal i:nth-child(2) { height: 3.5px; }
  .signal i:nth-child(3) { height: 5px; }
  .signal i:nth-child(4) { height: 6.5px; }
  .battery {
    width: 15px; height: 7px; border: 1px solid #fff; border-radius: 1.5px;
    padding: 1px; position: relative;
  }
  .battery::before { content: ""; display: block; height: 100%; width: 80%; background: #fff; }
  .battery::after {
    content: ""; position: absolute; right: -3px; top: 1.5px; width: 1.5px; height: 2.5px; background: #fff;
  }

  /* top banner ad */
  .ad-top {
    height: 50px;
    background: #fff;
    display: flex;
    align-items: stretch;
  }
  .ad-top .brand-cell {
    width: 48px;
    background: #111;
    display: flex;
    align-items: center;
    justify-content: center;
    color: var(--gold);
    font: 900 10px "Lato", sans-serif;
  }
  .ad-top .offer { flex: 1; padding: 3px 0 0 8px; color: var(--ink); }
  .offer-headline {
    font: 500 22px/1 "Cormorant Garamond", serif;
    letter-spacing: .5px;
  }
  .offer-headline sup { font-size: 12px; vertical-align: 8px; }
  .offer-sub { font: 400 7.5px/1.3 "Lato", sans-serif; color: #444; }
  .offer-cta {
    font: 700 6.5px "Lato", sans-serif; color: #222; display: flex; align-items: center; gap: 2px;
    margin-top: 1px;
  }
  .offer-cta::after {
    content: ""; width: 6px; height: 6px; background: var(--shop-yellow);
    clip-path: polygon(15% 0, 100% 50%, 15% 100%);
  }
  .ad-top .product-photo {
    width: 82px;
    background: radial-gradient(circle at 40% 45%, #f4a6bf 0%, #e2557e 45%, #a8163e 80%, #5c7a3a 100%);
  }

  /* main home area */
  .home { width: 270px; height: 248px; display: block; }
  .bubble circle { fill: url(#bubbleFill); filter: url(#bubbleShadow); }
  .bubble use { color: var(--red); }
  .bubble-label { font: 400 8.5px "Lato", sans-serif; fill: #444; text-anchor: middle; }
  .wordmark { font: 900 22px "Lato", sans-serif; fill: var(--red); text-anchor: middle; }
  .wordmark.top { font-size: 28px; }
  .tooltip rect { fill: #fff; stroke: #ccc; stroke-width: .6; }
  .tooltip text { font: 400 7px "Lato", sans-serif; fill: #555; text-anchor: middle; }

  /* bottom banner ad */
  .ad-bottom {
    height: 50px;
    background: #fff;
    display: flex;
    align-items: center;
    position: relative;
    padding-left: 5px;
  }
  .ad-bottom .brand-cell {
    display: flex; align-items: center; gap: 2px;
    color: var(--ad-green); font: 900 8px "Lato", sans-serif; width: 50px;
  }
  .ad-bottom .brand-cell::before {
    content: ""; width: 12px; height: 12px; border-radius: 50%; background: var(--ad-green); flex: none;
  }
  .ad-bottom .pitch { flex: 1; }
  .pitch-headline { font: 800 14.5px/1.1 "Nunito", sans-serif; color: #2b2b2b; }
  .pitch-headline em { font-style: normal; color: var(--ad-green-light); }
  .pitch-row { display: flex; align-items: center; justify-content: space-between; margin-top: 3px; padding-right: 3px; }
  .pitch-sub { font: 400 6.5px "Lato", sans-serif; color: #444; }
  .pitch-button {
    font: 700 6.5px "Lato", sans-serif; color: #fff; background: var(--ad-green);
    padding: 2px 4px; border-radius: 1px;
  }
  .ad-bottom .product-photo {
    width: 38px; height: 44px; align-self: flex-end;
    background: linear-gradient(160deg, #333 0%, #111 40%, #2f6d3a 100%);
    border-radius: 3px 3px 0 0;
  }
  .close-badge {
    position: absolute; right: 2px; top: -6px; width: 15px; height: 15px; border-radius: 50%;
    background: #fff; border: 1.5px solid #333; color: #222;
    font: 900 9px/12px "Lato", sans-serif; text-align: center;
  }

  /* tab bar */
  .tab-bar {
    height: 41px;
    background: linear-gradient(180deg, #c7434f 0%, var(--red-dark) 50%, var(--red-deep) 100%);
    display: flex;
    padding: 3px 2px;
  }
  .tab {
    flex: 1; display: flex; flex-direction: column; align-items: center; justify-content: center;
    color: #fff; font: 700 7.5px "Lato", sans-serif; gap: 2px;
  }
  .tab svg { width: 18px; height: 18px; fill: #fff; }
  .tab.is-active {
    background: linear-gradient(180deg, #a42330, #7d1420);
    border: 1px solid #b9505a;
    border-radius: 2px;
  }
</style>
</head>
<body>

<svg class="defs" aria-hidden="true">
  <defs>
    <radialGradient id="homeGlow" cx="50%" cy="50%" r="70%">
      <stop offset="0%" stop-color="#fbf8f0"/>
      <stop offset="45%" stop-color="#ebe3d0"/>
      <stop offset="100%" stop-color="#a89a78"/>
    </radialGradient>
    <radialGradient id="bubbleFill" cx="45%" cy="35%" r="65%">
      <stop offset="0%" stop-color="#ffffff"/>
      <stop offset="70%" stop-color="#ececec"/>
      <stop offset="100%" stop-color="#c9c9c9"/>
    </radialGradient>
    <filter id="bubbleShadow" x="-30%" y="-30%" width="160%" height="160%">
      <feDropShadow dx="0" dy="2" stdDeviation="2" flood-color="#000" flood-opacity=".35"/>
    </filter>
  </defs>
  <symbol id="ico-heart" viewBox="0 0 40 40">
    <path fill="currentColor" d="M20 35C8 26 3 19 3 12.5 3 7 7 3 12 3c3.5 0 6.5 2 8 5 1.5-3 4.5-5 8-5 5 0 9 4 9 9.5C37 19 32 26 20 35Z"/>
  </symbol>
  <symbol id="ico-search" viewBox="0 0 40 40">
    <circle cx="17" cy="17" r="11" fill="none" stroke="currentColor" stroke-width="5"/>
    <line x1="25" y1="25" x2="35" y2="35" stroke="currentColor" stroke-width="6" stroke-linecap="round"/>
  </symbol>
  <symbol id="ico-eye" viewBox="0 0 40 40">
    <path fill="currentColor" d="M2 20C8 10 14 7 20 7s12 3 18 13c-6 10-12 13-18 13S8 30 2 20Z"/>
    <circle cx="20" cy="20" r="9" fill="#fff"/>
    <circle cx="20" cy="20" r="5" fill="currentColor"/>
  </symbol>
  <symbol id="ico-mail" viewBox="0 0 40 40">
    <rect x="9" y="4" width="20" height="16" fill="#fff" stroke="currentColor" stroke-width="2"/>
    <path fill="currentColor" d="M3 13 20 25 37 13V35H3Z"/>
    <path d="M3 35 16 23M37 35 24 23" stroke="#fff" stroke-width="1.8"/>
  </symbol>
  <symbol id="ico-people" viewBox="0 0 40 40">
    <circle cx="27" cy="12" r="6.5" fill="currentColor"/>
    <path fill="currentColor" d="M16 35c0-9 4-14 11-14s11 5 11 14Z"/>
    <circle cx="13" cy="13" r="6.5" fill="currentColor" stroke="#fff" stroke-width="1.5"/>
    <path fill="currentColor" stroke="#fff" stroke-width="1.5" d="M2 36c0-9 4-14 11-14s11 5 11 14Z"/>
  </symbol>
  <symbol id="ico-clock" viewBox="0 0 40 40">
    <circle cx="20" cy="20" r="15" fill="#fff" stroke="currentColor" stroke-width="5"/>
    <path d="M20 10V21H28" fill="none" stroke="currentColor" stroke-width="4" stroke-linecap="round"/>
  </symbol>
  <symbol id="ico-chart" viewBox="0 0 40 40">
    <rect x="4" y="6" width="32" height="28" fill="#fff" stroke="currentColor" stroke-width="3.5"/>
    <polyline points="8,28 14,19 19,24 25,13 32,20" fill="none" stroke="currentColor" stroke-width="3"/>
  </symbol>
  <symbol id="ico-user" viewBox="0 0 40 40">
    <circle cx="20" cy="12" r="8" fill="currentColor"/>
    <path fill="currentColor" d="M5 38c0-11 6-16 15-16s15 5 15 16Z"/>
  </symbol>
  <symbol id="tab-home" viewBox="0 0 24 24">
    <path d="M12 3 2 12h3v9h5v-6h4v6h5v-9h3Z"/>
  </symbol>
  <symbol id="tab-mail" viewBox="0 0 24 24">
    <path d="M2 5h20v14H2Z M3.5 6.5 12 13l8.5-6.5" fill="#fff" stroke="#7d1420" stroke-width="1.2"/>
  </symbol>
  <symbol id="tab-power" viewBox="0 0 24 24">
    <path d="M7.5 5.5A8 8 0 1 0 16.5 5.5" fill="none" stroke="#fff" stroke-width="2.6" stroke-linecap="round"/>
    <line x1="12" y1="2.5" x2="12" y2="11" stroke="#fff" stroke-width="2.6" stroke-linecap="round"/>
  </symbol>
</svg>

<!-- Screen 1: labelled home menu -->
<section class="screen">
  <div class="status-bar">
    <span class="status-left"><span class="signal"><i></i><i></i><i></i><i></i></span>Telvo</span>
    <span>9:42 AM</span>
    <span class="battery"></span>
  </div>
  <div class="ad-top">
    <div class="brand-cell">Petalo</div>
    <div class="offer">
      <div class="offer-headline">SAVE 25<sup>%</sup></div>
      <div class="offer-sub">on Petalo Flowers, Plants &amp; Gifts</div>
      <div class="offer-cta">SHOP NOW</div>
    </div>
    <div class="product-photo" role="img" aria-label="Bouquet of pink and red roses"></div>
  </div>
  <svg class="home" viewBox="0 0 310 285">
    <rect width="310" height="285" fill="url(#homeGlow)"/>
    <g class="bubble"><circle cx="153" cy="43" r="31"/><use href="#ico-search" x="138" y="21" width="30" height="30"/><text class="bubble-label" x="153" y="61">Search</text></g>
    <g class="bubble"><circle cx="83" cy="74" r="31"/><use href="#ico-heart" x="68" y="52" width="30" height="30"/><text class="bubble-label" x="83" y="92">Favorites</text></g>
    <g class="bubble"><circle cx="224" cy="74" r="31"/><use href="#ico-eye" x="209" y="52" width="30" height="30"/><text class="bubble-label" x="224" y="92">ViewedMe</text></g>
    <g class="bubble"><circle cx="53" cy="146" r="31"/><use href="#ico-mail" x="38" y="124" width="30" height="30"/><text class="bubble-label" x="53" y="164">Messages</text></g>
    <g class="bubble"><circle cx="254" cy="146" r="31"/><use href="#ico-people" x="239" y="124" width="30" height="30"/><text class="bubble-label" x="254" y="164">Matches</text></g>
    <g class="bubble"><circle cx="83" cy="216" r="31"/><use href="#ico-chart" x="68" y="194" width="30" height="30"/><text class="bubble-label" x="83" y="234">Activity</text></g>
    <g class="bubble"><circle cx="224" cy="216" r="31"/><use href="#ico-clock" x="209" y="194" width="30" height="30"/><text class="bubble-label" x="224" y="234">History</text></g>
    <g class="bubble"><circle cx="153" cy="246" r="31"/><use href="#ico-user" x="138" y="224" width="30" height="30"/><text class="bubble-label" x="153" y="264">Profile</text></g>
    <text class="wordmark" x="153" y="154">Cool Nookz</text>
  </svg>
  <div class="ad-bottom">
    <div class="brand-cell">Brewly</div>
    <div class="pitch">
      <div class="pitch-headline">pay faster, <em>sip slower</em></div>
      <div class="pitch-row"><span class="pitch-sub">Brewly® mobile payment app</span><span class="pitch-button">Download Now</span></div>
    </div>
    <div class="product-photo" role="img" aria-label="Phone showing the payment app"></div>
    <span class="close-badge">×</span>
  </div>
  <nav class="tab-bar">
    <div class="tab"><svg><use href="#tab-home"/></svg>Home</div>
    <div class="tab"><svg><use href="#tab-mail"/></svg>Messages</div>
    <div class="tab is-active"><svg><use href="#tab-power"/></svg>Logout</div>
  </nav>
</section>

<!-- Screen 2: compact menu with wordmark on top -->
<section class="screen">
  <div class="status-bar">
    <span class="status-left"><span class="signal"><i></i><i></i><i></i><i></i></span>Telvo</span>
    <span>9:42 AM</span>
    <span class="battery"></span>
  </div>
  <div class="ad-top">
    <div class="brand-cell">Petalo</div>
    <div class="offer">
      <div class="offer-headline">SAVE 25<sup>%</sup></div>
      <div class="offer-sub">on Petalo Flowers, Plants &amp; Gifts</div>
      <div class="offer-cta">SHOP NOW</div>
    </div>
    <div class="product-photo" role="img" aria-label="Bouquet of pink and red roses"></div>
  </div>
  <svg class="home" viewBox="0 0 310 285">
    <rect width="310" height="285" fill="url(#homeGlow)"/>
    <text class="wordmark top" x="152" y="45">Cool Nookz</text>
    <g class="bubble"><circle cx="95" cy="116" r="25"/><use href="#ico-heart" x="82" y="103" width="26" height="26"/></g>
    <g class="bubble"><circle cx="152" cy="91" r="25"/><use href="#ico-search" x="139" y="78" width="26" height="26"/></g>
    <g class="bubble"><circle cx="209" cy="116" r="25"/><use href="#ico-eye" x="196" y="103" width="26" height="26"/></g>
    <g class="bubble"><circle cx="72" cy="173" r="25"/><use href="#ico-mail" x="59" y="160" width="26" height="26"/></g>
    <g class="bubble"><circle cx="232" cy="173" r="25"/><use href="#ico-people" x="219" y="160" width="26" height="26"/></g>
    <g class="bubble"><circle cx="95" cy="230" r="25"/><use href="#ico-chart" x="82" y="217" width="26" height="26"/></g>
    <g class="bubble"><circle cx="209" cy="230" r="25"/><use href="#ico-clock" x="196" y="217" width="26" height="26"/></g>
    <g class="bubble"><circle cx="152" cy="254" r="25"/><use href="#ico-user" x="139" y="241" width="26" height="26"/></g>
  </svg>
  <div class="ad-bottom">
    <div class="brand-cell">Brewly</div>
    <div class="pitch">
      <div class="pitch-headline">pay faster, <em>sip slower</em></div>
      <div class="pitch-row"><span class="pitch-sub">Brewly® mobile payment app</span><span class="pitch-button">Download Now</span></div>
    </div>
    <div class="product-photo" role="img" aria-label="Phone showing the payment app"></div>
    <span class="close-badge">×</span>
  </div>
  <nav class="tab-bar">
    <div class="tab"><svg><use href="#tab-home"/></svg>Home</div>
    <div class="tab"><svg><use href="#tab-mail"/></svg>Messages</div>
    <div class="tab is-active"><svg><use href="#tab-power"/></svg></div>
  </nav>
</section>

<!-- Screen 3: icon menu with hover tooltip -->
<section class="screen">
  <div class="status-bar">
    <span class="status-left"><span class="signal"><i></i><i></i><i></i><i></i></span>Telvo</span>
    <span>9:42 AM</span>
    <span class="battery"></span>
  </div>
  <div class="ad-top">
    <div class="brand-cell">Petalo</div>
    <div class="offer">
      <div class="offer-headline">SAVE 25<sup>%</sup></div>
      <div class="offer-sub">on Petalo Flowers, Plants &amp; Gifts</div>
      <div class="offer-cta">SHOP NOW</div>
    </div>
    <div class="product-photo" role="img" aria-label="Bouquet of pink and red roses"></div>
  </div>
  <svg class="home" viewBox="0 0 310 285">
    <rect width="310" height="285" fill="url(#homeGlow)"/>
    <g class="bubble"><circle cx="153" cy="44" r="31"/><use href="#ico-search" x="136" y="27" width="34" height="34"/></g>
    <g class="tooltip"><rect x="127" y="1" width="52" height="12"/><text x="153" y="10">Search</text></g>
    <g class="bubble"><circle cx="82" cy="75" r="31"/><use href="#ico-heart" x="65" y="58" width="34" height="34"/></g>
    <g class="bubble"><circle cx="223" cy="75" r="31"/><use href="#ico-eye" x="206" y="58" width="34" height="34"/></g>
    <g class="bubble"><circle cx="53" cy="146" r="31"/><use href="#ico-mail" x="36" y="129" width="34" height="34"/></g>
    <g class="bubble"><circle cx="253" cy="146" r="31"/><use href="#ico-people" x="236" y="129" width="34" height="34"/></g>
    <g class="bubble"><circle cx="82" cy="216" r="31"/><use href="#ico-chart" x="65" y="199" width="34" height="34"/></g>
    <g class="bubble"><circle cx="223" cy="216" r="31"/><use href="#ico-clock" x="206" y="199" width="34" height="34"/></g>
    <g class="bubble"><circle cx="153" cy="246" r="31"/><use href="#ico-user" x="136" y="229" width="34" height="34"/></g>
    <text class="wordmark" x="153" y="154">Cool Nookz</text>
  </svg>
  <div class="ad-bottom">
    <div class="brand-cell">Brewly</div>
    <div class="pitch">
      <div class="pitch-headline">pay faster, <em>sip slower</em></div>
      <div class="pitch-row"><span class="pitch-sub">Brewly® mobile payment app</span><span class="pitch-button">Download Now</span></div>
    </div>
    <div class="product-photo" role="img" aria-label="Phone showing the payment app"></div>
    <span class="close-badge">×</span>
  </div>
  <nav class="tab-bar">
    <div class="tab"><svg><use href="#tab-home"/></svg>Home</div>
    <div class="tab"><svg><use href="#tab-mail"/></svg>Messages</div>
    <div class="tab is-active"><svg><use href="#tab-power"/></svg>Logout</div>
  </nav>
</section>

<!-- Screen 4: icon menu with centred wordmark -->
<section class="screen">
  <div class="status-bar">
    <span class="status-left"><span class="signal"><i></i><i></i><i></i><i></i></span>Telvo</span>
    <span>9:42 AM</span>
    <span class="battery"></span>
  </div>
  <div class="ad-top">
    <div class="brand-cell">Petalo</div>
    <div class="offer">
      <div class="offer-headline">SAVE 25<sup>%</sup></div>
      <div class="offer-sub">on Petalo Flowers, Plants &amp; Gifts</div>
      <div class="offer-cta">SHOP NOW</div>
    </div>
    <div class="product-photo" role="img" aria-label="Bouquet of pink and red roses"></div>
  </div>
  <svg class="home" viewBox="0 0 310 285">
    <rect width="310" height="285" fill="url(#homeGlow)"/>
    <g class="bubble"><circle cx="153" cy="44" r="31"/><use href="#ico-search" x="136" y="27" width="34" height="34"/></g>
    <g class="bubble"><circle cx="82" cy="75" r="31"/><use href="#ico-heart" x="65" y="58" width="34" height="34"/></g>
    <g class="bubble"><circle cx="223" cy="75" r="31"/><use href="#ico-eye" x="206" y="58" width="34" height="34"/></g>
    <g class="bubble"><circle cx="53" cy="146" r="31"/><use href="#ico-mail" x="36" y="129" width="34" height="34"/></g>
    <g class="bubble"><circle cx="253" cy="146" r="31"/><use href="#ico-people" x="236" y="129" width="34" height="34"/></g>
    <g class="bubble"><circle cx="82" cy="216" r="31"/><use href="#ico-chart" x="65" y="199" width="34" height="34"/></g>
    <g class="bubble"><circle cx="223" cy="216" r="31"/><use href="#ico-clock" x="206" y="199" width="34" height="34"/></g>
    <g class="bubble"><circle cx="153" cy="246" r="31"/><use href="#ico-user" x="136" y="229" width="34" height="34"/></g>
    <text class="wordmark" x="153" y="154">Cool Nookz</text>
  </svg>
  <div class="ad-bottom">
    <div class="brand-cell">Brewly</div>
    <div class="pitch">
      <div class="pitch-headline">pay faster, <em>sip slower</em></div>
      <div class="pitch-row"><span class="pitch-sub">Brewly® mobile payment app</span><span class="pitch-button">Download Now</span></div>
    </div>
    <div class="product-photo" role="img" aria-label="Phone showing the payment app"></div>
    <span class="close-badge">×</span>
  </div>
  <nav class="tab-bar">
    <div class="tab"><svg><use href="#tab-home"/></svg>Home</div>
    <div class="tab"><svg><use href="#tab-mail"/></svg>Messages</div>
    <div class="tab is-active"><svg><use href="#tab-power"/></svg>Logout</div>
  </nav>
</section>

</body>
</html>
```